Business Card & Stationary Design Project

We are looking for some creative direction for business cards and our stationary.

We are a global logistics firm that has recently changed its name to Marwick Global Logistics and we have a new website due out tomorrow (www.marwick.com.au).

The colours of the company are rich navy tones, I would like to have business cards that fit together to make one picture on the back (possibly an old map of the world??), and the front to be modern contemporary looking.

But I am open to suggestions, so just incorporate our new logo and get going!
Updates

Hi Everyone,

Thank you for all of your designs so far and the time you have put into it.

I have asked many of you for amendments to see if we can get a final product, so with this in mind I am extending the deadline by a few days.

Good luck and thank you once again.

Please message me direct if you need any clarification.

Kind Regards
Tobias

Reason: As outlined the extra 3 days is for amendments and changes to the current submissions. Thanks Tobias

Industry/Entity Type

Business

```html
<!DOCTYPE html>
<html lang="en">
<head>
<meta charset="utf-8">
<title>Marwick Global Logistics – Business Card</title>
<link rel="stylesheet" href="https://fonts.googleapis.com/css2?family=Arimo:wght@400;700&display=swap">
<style>
  :root {
    --navy: #0e3d66;
    --navy-deep: #0a2c4c;
    --teal-dark: #0f3f4a;
    --teal: #2a6e7c;
    --teal-light: #5f98a3;
    --ink: #2b2b2b;
    --paper: #ffffff;
    --backdrop: #e9eaec;
  }
  * { box-sizing: border-box; margin: 0; padding: 0; }
  html, body {
    width: 900px; height: 1200px; overflow: hidden;
    background: var(--backdrop);
    font-family: "Arimo", Arial, sans-serif;
  }
  .canvas {
    position: relative; width: 900px; height: 1200px;
  }
  .card {
    position: absolute; left: 70px;
    width: 760px; height: 434px;
    background: var(--paper);
    box-shadow: 0 14px 36px rgba(0,0,0,0.18), 0 2px 6px rgba(0,0,0,0.08);
    overflow: hidden;
  }
  .card--front { top: 110px; }
  .card--back { top: 656px; }

  /* Front */
  .front-photo {
    position: absolute; inset: 0;
    background:
      linear-gradient(90deg, rgba(8,40,48,0.35) 0 10%, transparent 10% 22%, rgba(8,40,48,0.3) 22% 26%, transparent 26%),
      linear-gradient(180deg, var(--teal-dark) 0%, var(--teal) 55%, var(--teal-light) 78%, var(--teal) 100%);
  }
  .brand-tab {
    position: absolute; right: 0; top: 138px;
    width: 330px; height: 96px;
    background: var(--paper);
    clip-path: polygon(28px 0, 100% 0, 100% 100%, 28px 100%, 0 50%);
    display: flex; align-items: center; padding-left: 46px;
  }

  /* Brand lockup */
  .brand {
    display: flex; align-items: center; gap: 10px;
  }
  .brand__name {
    color: var(--navy);
    font-weight: 700; font-size: 17px;
    letter-spacing: 0.06em; white-space: nowrap;
  }
  .brand__dot {
    width: 30px; height: 30px; border-radius: 50%;
    background: var(--navy); flex: none;
  }

  /* Back */
  .back-brand { position: absolute; top: 40px; right: 40px; }
  .person { position: absolute; left: 46px; top: 40px; }
  .person__name { font-weight: 700; font-size: 18px; color: var(--ink); }
  .person__role { font-weight: 700; font-size: 18px; color: var(--navy); margin-top: 2px; }

  .contacts { position: absolute; left: 46px; top: 130px; list-style: none; }
  .contact {
    display: flex; align-items: center; gap: 18px;
    height: 48px; font-size: 19px; color: var(--ink); letter-spacing: 0.02em;
  }
  .icon {
    width: 34px; height: 34px; border-radius: 50%;
    background: var(--navy); flex: none;
    display: flex; align-items: center; justify-content: center;
  }
  .icon svg { width: 18px; height: 18px; }

  .address {
    position: absolute; left: 400px; top: 200px;
    display: flex; gap: 18px; align-items: flex-start;
  }
  .address__lines { font-size: 19px; line-height: 1.3; color: var(--ink); letter-spacing: 0.02em; }
</style>
</head>
<body>
<main class="canvas">

  <section class="card card--front" aria-label="Card front">
    <div class="front-photo" role="img" aria-label="Teal duotone photograph of a port warehouse with stacked shipping containers"></div>
    <div class="brand-tab">
      <div class="brand">
        <span class="brand__name">MARWICK GLOBAL LOGISTICS</span>
        <span class="brand__dot"></span>
      </div>
    </div>
  </section>

  <section class="card card--back" aria-label="Card back">
    <div class="person">
      <p class="person__name">Daniel Hart</p>
      <p class="person__role">Managing Director</p>
    </div>

    <div class="brand back-brand">
      <span class="brand__name">MARWICK GLOBAL LOGISTICS</span>
      <span class="brand__dot"></span>
    </div>

    <ul class="contacts">
      <li class="contact">
        <span class="icon"><svg viewBox="0 0 24 24"><path fill="#fff" d="M6.6 2.5l3 3.2-1.8 2.4c1.2 2.6 3.5 4.9 6.1 6.1l2.4-1.8 3.2 3-1.7 3.7C10.6 19.4 4.6 13.4 3 5.3z"/></svg></span>
        <span>+61 2 9460 2175</span>
      </li>
      <li class="contact">
        <span class="icon"><svg viewBox="0 0 24 24"><rect x="3" y="6" width="18" height="12" fill="#fff"/><path d="M3 6l9 7 9-7" fill="none" stroke="var(--navy)" stroke-width="1.6"/></svg></span>
        <span>daniel@marwick.com.au</span>
      </li>
      <li class="contact">
        <span class="icon"><svg viewBox="0 0 24 24" fill="none" stroke="#fff" stroke-width="1.6"><circle cx="12" cy="12" r="9"/><ellipse cx="12" cy="12" rx="4" ry="9"/><path d="M3 12h18"/></svg></span>
        <span>www.marwick.com.au</span>
      </li>
    </ul>

    <div class="address">
      <span class="icon"><svg viewBox="0 0 24 24"><path fill="#fff" d="M12 2a7 7 0 0 0-7 7c0 5 7 13 7 13s7-8 7-13a7 7 0 0 0-7-7z"/><circle cx="12" cy="9" r="2.6" fill="var(--navy)"/></svg></span>
      <p class="address__lines">86 Wharf Road<br>Millers Point NSW<br>2000</p>
    </div>
  </section>

</main>
</body>
</html>
```